Green blog

Hi there !
I want to redesign my french green blog here: http://www.verdanimo.info

I want the same presentation, but something much funny, professionnal and great !

I have a new logo to integrate it, i'll put it on the attachment.

Thank you so much for your work in advance !

Hello there !

The price is for only the design, not the wordpress integration !

Thanks

```html
<!DOCTYPE html>
<html lang="fr">
<head>
<meta charset="utf-8">
<title>Verdanimo – Penser nature</title>
<link rel="stylesheet" href="https://fonts.googleapis.com/css2?family=Questrial&family=Arimo:wght@400;700&display=swap">
<style>
:root{
  --header-top:#6f8a1e;
  --header-bottom:#4f6a0e;
  --page-bg:#e9e6c6;
  --sidebar-bg:#e2dfbc;
  --title-band:#dfdcbd;
  --title-green:#2f4a12;
  --text:#2b2b1a;
  --muted:#8c8c62;
  --badge:#55621a;
  --logo-green:#a9bd2b;
  --link-red:#8a0a0a;
  --rule:#c9c9a0;
  --tab-dark:#1c1c1a;
  --tab-light:#8b9a5e;
}
*{box-sizing:border-box;margin:0;padding:0}
html,body{width:1200px;height:900px;overflow:hidden}
body{background:var(--page-bg);font-family:"Arimo",Arial,sans-serif;color:var(--text);position:relative}

.site-header{position:absolute;left:0;top:0;width:1200px;height:142px;background:linear-gradient(180deg,var(--header-top),var(--header-bottom));border-bottom:2px solid #f3f1d8}
.brand{position:absolute;left:140px;top:40px;display:flex;align-items:center;gap:14px}
.brand-dot{width:70px;height:70px;border-radius:50%;background:#8fa02a}
.brand-name{font-family:"Questrial",sans-serif;font-size:44px;color:var(--logo-green)}

.main-nav{position:absolute;top:0;left:535px;display:flex;gap:4px}
.main-nav a{display:block;width:131px;height:29px;line-height:27px;text-align:center;color:#fff;font-family:"Arimo",sans-serif;font-size:15px;text-decoration:none;border-radius:0 0 6px 6px;background:linear-gradient(180deg,#a7b57a,var(--tab-light));border:1px solid #5a6a2a;border-top:none}
.main-nav a.active{background:linear-gradient(180deg,#4a4a46,var(--tab-dark));border-color:#000}

.sidebar{position:absolute;left:820px;top:144px;width:253px;height:756px;background:var(--sidebar-bg)}

.post{position:absolute;left:128px;width:670px}
.post-title{height:40px;background:linear-gradient(90deg,var(--title-band),rgba(223,220,189,.3));border-bottom:1px solid var(--rule);font-family:"Questrial",sans-serif;font-size:26px;color:var(--title-green);font-weight:400;padding-left:185px;line-height:40px}
.post-thumb{position:absolute;left:20px;top:122px;width:97px;height:58px;border-radius:40%;background:radial-gradient(ellipse,#9fb4c8,#c9d3d8 60%,transparent 70%)}
.post-body{position:absolute;left:187px;top:80px;width:385px;font-size:13px;line-height:22px}
.read-more{position:absolute;font-weight:700;font-size:13px;color:var(--link-red);text-decoration:none;display:flex;align-items:center;gap:8px}
.retweet{position:absolute;left:582px;top:86px;width:68px;text-align:center}
.retweet-count{display:block;height:62px;position:relative;font-size:20px;color:var(--badge)}
.retweet-count svg{position:absolute;left:0;top:0}
.retweet-count span{position:relative;top:12px}
.retweet-label{display:block;margin-top:8px;background:var(--badge);color:#fff;font-size:12px;line-height:17px}
.post-meta{position:absolute;left:22px;width:670px;font-size:11px;color:#3a3a22;display:flex;align-items:center}
.post-meta .date{width:165px}
.post-meta .item{display:flex;align-items:center;gap:6px;margin-right:20px}
.post-rule{position:absolute;left:-5px;width:675px;border-top:1px solid var(--rule)}

.widget-title{position:absolute;font-family:"Questrial",sans-serif;font-size:19px;color:#35501a;font-weight:400}
.search-box{position:absolute;left:18px;top:78px;width:192px;height:21px;background:#fff;border-radius:3px;font-size:11px;color:#aaa;padding:3px 11px}
.search-box svg{position:absolute;right:4px;top:2px}
.widget-rule{position:absolute;left:15px;width:230px;border-top:1px solid #c9c7a0}
.recent-list{position:absolute;left:18px;top:174px;list-style:none;width:220px}
.recent-list li{display:flex;gap:18px;font-size:13px;line-height:16px;color:var(--muted);margin-bottom:15px}
.recent-list li::before{content:"";flex:none;width:12px;height:12px;border-radius:50%;background:#8a8a60;margin-top:2px;clip-path:none}
.solar-text{position:absolute;left:18px;top:422px;width:225px;font-size:13px;line-height:20px;color:var(--muted)}
.solar-more{left:146px;top:486px;color:#3a3a22;font-weight:400}
.info-list{position:absolute;left:23px;top:592px;list-style:none}
.info-list li{font-size:13px;line-height:20px;color:var(--muted);padding-left:22px;position:relative}
.info-list li::before{content:"";position:absolute;left:0;top:5px;border-left:8px solid #4e5a1a;border-top:4px solid transparent;border-bottom:4px solid transparent}
</style>
</head>
<body>

<header class="site-header">
  <div class="brand"><span class="brand-dot"></span><span class="brand-name">Verdanimo</span></div>
  <nav class="main-nav">
    <a class="active" href="#">Produits écolo</a>
    <a href="#">Newsletter</a>
    <a href="#">Gestes simples</a>
    <a href="#">A propos</a>
  </nav>
</header>

<article class="post" style="top:182px;height:320px">
  <h2 class="post-title">Astuce 8: Récupération d’eau</h2>
  <div class="post-thumb" role="img" aria-label="Illustration d’un chapeau posé dans une flaque d’eau"></div>
  <div class="post-body">
    Dans la catégorie: Manger bien Comment bien choisir son saumon?<br>
    Croustillant et bluffant Creative Commons License photo credit: photomimosa<br>
    Je suis tombé aujourd’hui sur un article de grande qualité, que je souhaite donc partager avec vous !<br>
    Il vous informera de manière précise sur le saumon, ce poissons que nous aimons particulièrement en France.
  </div>
  <a class="read-more" href="#" style="left:477px;top:264px">lire la suite <svg width="16" height="10" viewBox="0 0 16 10"><path d="M1 9 Q3 3 11 3 V0 L16 4.5 11 9 V6 Q5 6 1 9Z" fill="#8a0a0a"/></svg></a>
  <div class="retweet">
    <span class="retweet-count"><svg width="68" height="64" viewBox="0 0 68 64"><path d="M3 3H65V48H30L18 61V48H3Z" fill="none" stroke="#55621a" stroke-width="6"/></svg><span>1</span></span>
    <span class="retweet-label">retweet</span>
  </div>
  <div class="post-meta" style="top:294px">
    <span class="date">juillet 24th, 2010</span>
    <span class="item"><svg width="14" height="13" viewBox="0 0 14 13"><circle cx="7" cy="4" r="3.5" fill="#3a3a22"/><path d="M0 13Q7 4 14 13Z" fill="#3a3a22"/></svg>Léa Verdier</span>
    <span class="item"><svg width="13" height="12" viewBox="0 0 13 12"><ellipse cx="6.5" cy="5" rx="6.5" ry="5" fill="#3a3a22"/><path d="M3 8L2 12 7 9Z" fill="#3a3a22"/></svg>10</span>
    <span class="item"><svg width="14" height="10" viewBox="0 0 14 10"><path d="M0 1Q0 0 1 0H9L14 5 9 10H1Q0 10 0 9Z" fill="#3a3a22"/></svg>arrosage . eau . jardin . récupérer de l’eau</span>
  </div>
  <div class="post-rule" style="top:314px"></div>
</article>

<article class="post" style="top:535px;height:320px">
  <h2 class="post-title">Astuce 8: Récupération d’eau</h2>
  <div class="post-body">
    Dans la catégorie: Manger bien Comment bien choisir son saumon?<br>
    Croustillant et bluffant Creative Commons License photo credit: photomimosa<br>
    Je suis tombé aujourd’hui sur un article de grande qualité, que je souhaite donc partager avec vous !<br>
    Il vous informera de manière précise sur le saumon, ce poissons que nous aimons particulièrement en France.
  </div>
  <a class="read-more" href="#" style="left:480px;top:259px">lire la suite <svg width="16" height="10" viewBox="0 0 16 10"><path d="M1 9 Q3 3 11 3 V0 L16 4.5 11 9 V6 Q5 6 1 9Z" fill="#8a0a0a"/></svg></a>
  <div class="retweet">
    <span class="retweet-count"><svg width="68" height="64" viewBox="0 0 68 64"><path d="M3 3H65V48H30L18 61V48H3Z" fill="none" stroke="#55621a" stroke-width="6"/></svg><span>1</span></span>
    <span class="retweet-label">retweet</span>
  </div>
  <div class="post-meta" style="top:293px">
    <span class="date">juillet 24th, 2010</span>
    <span class="item"><svg width="14" height="13" viewBox="0 0 14 13"><circle cx="7" cy="4" r="3.5" fill="#3a3a22"/><path d="M0 13Q7 4 14 13Z" fill="#3a3a22"/></svg>Léa Verdier</span>
    <span class="item"><svg width="13" height="12" viewBox="0 0 13 12"><ellipse cx="6.5" cy="5" rx="6.5" ry="5" fill="#3a3a22"/><path d="M3 8L2 12 7 9Z" fill="#3a3a22"/></svg>10</span>
    <span class="item"><svg width="14" height="10" viewBox="0 0 14 10"><path d="M0 1Q0 0 1 0H9L14 5 9 10H1Q0 10 0 9Z" fill="#3a3a22"/></svg>arrosage . eau . jardin . récupérer de l’eau</span>
  </div>
  <div class="post-rule" style="top:313px"></div>
</article>

<article class="post" style="top:880px;height:20px;overflow:hidden">
  <h2 class="post-title">Astuce 8: Récupération d’eau</h2>
</article>

<aside class="sidebar">
  <h3 class="widget-title" style="left:18px;top:43px">Search</h3>
  <div class="search-box">search<svg width="16" height="16" viewBox="0 0 16 16"><circle cx="6.5" cy="6.5" r="5" fill="none" stroke="#999" stroke-width="2"/><path d="M10 10L15 15" stroke="#999" stroke-width="2.5"/></svg></div>
  <div class="widget-rule" style="top:121px"></div>

  <h3 class="widget-title" style="left:18px;top:140px">Articles récents</h3>
  <ul class="recent-list">
    <li>Comment bien choisir son saumon?</li>
    <li>Astuce 8: Récupération d’eau</li>
    <li>Un écologiste tibétain en prison</li>
    <li>La crise ne doit pas faire oublier l’écologie</li>
    <li>Astuce 7: Faire fuir les fourmis</li>
  </ul>
  <div class="widget-rule" style="top:366px"></div>

  <h3 class="widget-title" style="left:18px;top:396px">Energie solaire</h3>
  <p class="solar-text">Retrouvez toutes nos informations sur l’énergie solaire ici. (panneaux photo-voltaïques, système d’énergie solaires...)</p>
  <a class="read-more solar-more" href="#">lire la suite <svg width="16" height="10" viewBox="0 0 16 10"><path d="M1 9 Q3 3 11 3 V0 L16 4.5 11 9 V6 Q5 6 1 9Z" fill="#3a3a22"/></svg></a>
  <div class="widget-rule" style="top:538px;left:12px"></div>

  <h3 class="widget-title" style="left:21px;top:558px">Informations</h3>
  <ul class="info-list">
    <li>A propos</li>
    <li>Covoiturage</li>
    <li>Devenez rédacteur</li>
    <li>Du bio pour votre bébé</li>
    <li>Economie d’énergie</li>
    <li>Economie de l’eau</li>
    <li>Energie solaire</li>
    <li>Gestes simples</li>
    <li>Guide pratique</li>
  </ul>
</aside>

</body>
</html>
```